Bright Path Rehabilitation Stationary
Business Card, Letter Head, Envelope, Fax Cover, Invoice & Referral/Prescription Pad
Bright Path Rehabilitation Stationary  -
Creative Brief
Use specific fonts
Please use standard or same font as in logo
Simple
Gregory Lindqvist
Marketing/Administrative Director
27415 PT Hargrove Blvd # D Palo Mesa North, AZ 85291
gregory@brightpathrehab.com
www.brightpathrehab.com
Please include on the front of the card "Comprehensive Outpatient Rehabilitation Facility".Physical Therapy and Psych/Social Services. Please draw up another business card with same information except Monica Lindqvist with a title of Physical Therapist. For the fax cover sheet, envelope, referral/prescription pad and letter head please incorporate logo. We have included a map as well for referral/prescription pads.
Hands on Approach Individualized Plan of Care Friendly, Caring Staff

```html
<!DOCTYPE html>
<html lang="en">
<head>
<meta charset="utf-8">
<title>Bright Path Rehabilitation Stationery</title>
<link href="https://fonts.googleapis.com/css2?family=Arimo:wght@400;700&display=swap" rel="stylesheet">
<style>
  :root {
    --blue-deep: #1b4f9c;
    --blue-mid: #2f78c4;
    --blue-light: #6fb3e6;
    --band-pale: #cfe6f7;
    --ink: #3a3a3a;
    --muted: #8c8c8c;
    --card-dark: #1c1d26;
    --card-dark-2: #2b2d3a;
    --paper: #ffffff;
    --edge: #d6d6d6;
  }
  * { margin: 0; padding: 0; box-sizing: border-box; }
  html, body { width: 1200px; height: 628px; overflow: hidden; background: var(--paper); }
  body { position: relative; font-family: "Arimo", Arial, sans-serif; color: var(--ink); }

  .brand-name { font-family: "Arimo", Arial, sans-serif; font-weight: 700; color: var(--blue-deep); letter-spacing: 0.5px; display: flex; align-items: center; gap: 6px; }
  .brand-dot { display: inline-block; border-radius: 50%; background: var(--blue-deep); }
  .brand-name.on-dark { color: var(--blue-light); }
  .brand-name.on-dark .brand-dot { background: var(--blue-light); }

  /* Business card – front */
  .card-front { position: absolute; left: 0; top: 331px; width: 173px; height: 136px; background: linear-gradient(135deg, var(--card-dark-2), var(--card-dark)); }
  .card-front .brand-name { position: absolute; left: 38px; top: 40px; width: 110px; font-size: 10px; line-height: 1.2; }
  .card-front .brand-dot { width: 14px; height: 14px; flex: none; }
  .card-front .contact { position: absolute; left: 10px; bottom: 14px; font-size: 4.5px; line-height: 1.5; color: #cfd3dc; }

  /* Business card – back */
  .card-back { position: absolute; left: 0; top: 468px; width: 173px; height: 132px; background: var(--paper); border: 1px solid var(--edge); overflow: hidden; }
  .card-back .wave { position: absolute; inset: 0; }
  .card-back .holder { position: absolute; right: 10px; top: 12px; text-align: right; font-size: 5px; line-height: 1.4; color: #ffffff; }
  .card-back .holder strong { font-size: 6px; }
  .card-back .brand-name { position: absolute; left: 8px; top: 46px; font-size: 6.5px; }
  .card-back .brand-dot { width: 7px; height: 7px; }
  .card-back .details { position: absolute; left: 10px; top: 68px; font-size: 4.5px; line-height: 1.5; color: var(--ink); }
  .card-back .services { position: absolute; left: 0; bottom: 8px; width: 100%; padding-left: 10px; font-size: 5.5px; font-weight: 700; color: #ffffff; }

  /* Letterhead */
  .letterhead { position: absolute; left: 173px; top: 0; width: 480px; height: 628px; background: var(--paper); border: 1px solid var(--edge); }
  .letterhead .brand-name { position: absolute; left: 58px; top: 44px; font-size: 13px; }
  .letterhead .brand-dot { width: 12px; height: 12px; }
  .letterhead .web { position: absolute; right: 48px; top: 26px; text-align: right; font-size: 6px; line-height: 1.5; color: var(--muted); }
  .letterhead .footer-contact { position: absolute; left: 30px; bottom: 52px; font-size: 5.5px; line-height: 1.6; color: var(--ink); }
  .letterhead .band { position: absolute; left: 10px; right: 10px; bottom: 10px; height: 34px; background: linear-gradient(90deg, var(--blue-mid), var(--blue-light) 70%, var(--band-pale)); display: flex; align-items: center; padding-left: 18px; }
  .band-text { font-size: 13px; font-weight: 700; color: #ffffff; }
  .letterhead .corner-mark { position: absolute; right: 40px; bottom: 54px; width: 30px; height: 30px; border-radius: 50%; background: var(--blue-deep); }

  /* Envelope – back */
  .envelope-back { position: absolute; left: 684px; top: 72px; width: 516px; height: 240px; }
  .envelope-back svg { position: absolute; inset: 0; }
  .envelope-back .brand-name { position: absolute; left: 0; width: 100%; top: 96px; justify-content: center; font-size: 10px; }
  .envelope-back .brand-dot { width: 10px; height: 10px; }

  /* Envelope – front */
  .envelope-front { position: absolute; left: 684px; top: 324px; width: 516px; height: 276px; background: var(--paper); border: 1px solid var(--edge); }
  .envelope-front .brand-name { position: absolute; left: 24px; top: 34px; font-size: 12px; }
  .envelope-front .brand-dot { width: 11px; height: 11px; }
  .envelope-front .return { position: absolute; left: 24px; top: 160px; font-size: 5.5px; line-height: 1.6; color: var(--ink); }
  .envelope-front .band { position: absolute; left: 0; right: 0; bottom: 18px; height: 30px; background: linear-gradient(90deg, var(--blue-light), var(--band-pale) 80%); display: flex; align-items: center; padding-left: 24px; }
  .envelope-front .band .band-text { color: var(--blue-deep); font-size: 12px; }
  .envelope-front .corner-mark { position: absolute; right: 30px; bottom: 52px; width: 36px; height: 36px; border-radius: 50%; background: var(--blue-deep); }
</style>
</head>
<body>

  <section class="card-front" aria-label="Business card front">
    <div class="brand-name on-dark"><span class="brand-dot"></span>Bright Path Rehabilitation</div>
    <div class="contact">gregory@brightpathrehab.com<br>www.brightpathrehab.com</div>
  </section>

  <section class="card-back" aria-label="Business card back">
    <svg class="wave" viewBox="0 0 173 132" preserveAspectRatio="none" aria-hidden="true">
      <defs>
        <linearGradient id="cardWave" x1="0" y1="0" x2="1" y2="0">
          <stop offset="0" stop-color="#6fb3e6"/>
          <stop offset="1" stop-color="#1b4f9c"/>
        </linearGradient>
      </defs>
      <path d="M60 0 H173 V58 C140 48 100 44 60 40 Z" fill="url(#cardWave)"/>
      <rect x="0" y="112" width="173" height="20" fill="url(#cardWave)"/>
    </svg>
    <div class="holder"><strong>Gregory Lindqvist</strong><br>Marketing/Administrative Director</div>
    <div class="brand-name"><span class="brand-dot"></span>Bright Path Rehabilitation</div>
    <div class="details">Ph: (623) 555-0148<br>Fax: (623) 555-0149<br>27415 PT Hargrove Blvd # D<br>Palo Mesa North, AZ 85291</div>
    <div class="services">Physical Therapy and Psych/Social Services</div>
  </section>

  <section class="letterhead" aria-label="Letterhead">
    <div class="brand-name"><span class="brand-dot"></span>Bright Path Rehabilitation</div>
    <div class="web">gregory@brightpathrehab.com<br>www.brightpathrehab.com</div>
    <div class="footer-contact">Ph: (623) 555-0148<br>Fax: (623) 555-0149<br><br>27415 PT Hargrove Blvd # D<br>Palo Mesa North, AZ 85291</div>
    <span class="corner-mark" aria-hidden="true"></span>
    <div class="band"><span class="band-text">Physical Therapy and Psych/Social Services</span></div>
  </section>

  <section class="envelope-back" aria-label="Envelope back">
    <svg viewBox="0 0 516 240" aria-hidden="true">
      <rect x="0.5" y="0.5" width="515" height="239" fill="#ffffff" stroke="#d6d6d6"/>
      <path d="M0.5 0.5 L0.5 70 Q0.5 90 20 100 L240 150 Q258 154 276 150 L496 100 Q515.5 90 515.5 70 L515.5 0.5" fill="none" stroke="#c8c8c8" stroke-width="1"/>
    </svg>
    <div class="brand-name"><span class="brand-dot"></span>Bright Path Rehabilitation</div>
  </section>

  <section class="envelope-front" aria-label="Envelope front">
    <div class="brand-name"><span class="brand-dot"></span>Bright Path Rehabilitation</div>
    <div class="return">27415 PT Hargrove Blvd # D &nbsp;Palo Mesa North, AZ 85291<br>Ph: (623) 555-0148 &nbsp;Fax: (623) 555-0149</div>
    <span class="corner-mark" aria-hidden="true"></span>
    <div class="band"><span class="band-text">Physical Therapy and Psych/Social Services</span></div>
  </section>

</body>
</html>
```